2017 Massachusetts Patrol Deputy Statute Digest Cover

Each year I put out a new Patrol Deputy Statute Digest. I'm looking for a new design for 2017. I like to change the look each year. I've included the last couple of years versions as samples along with my logos. I like the 2016 version much better than the 2016. Incorporating an actual image is a plus. The book is also geared specifically to Massachusetts Police Officers.

Target Market(s)

Massachusetts Police officers

Font styles to use
Serif
Other font styles liked:
• designer choice

Requirements
Must have
• Eye popping design that is professional and not too flashy. Back cover and spine is also needed.
Nice to have
• Photo image(s)
Should not have
• Copyright protected images or images that identify a specific police agency as I would require their permission.

```html
<!DOCTYPE html>
<html lang="en">
<head>
<meta charset="utf-8">
<title>Patrol Deputy Statute Digest 2017 – Spine and Cover</title>
<link rel="stylesheet" href="https://fonts.googleapis.com/css2?family=Anton&family=Tinos:wght@400;700&display=swap">
<style>
  :root {
    --page-bg: #d6d6d6;
    --cover-red: #b81418;
    --year-red: #c4161c;
    --title-white: #ffffff;
    --steel-dark: #2c3440;
    --steel-mid: #7d8794;
    --steel-light: #c9ced4;
    --police-blue: #1d5fb0;
    --copyright-gold: #e8c24a;
    --badge-navy: #24324e;
    --author-ink: #1b1b1b;
  }
  * { box-sizing: border-box; margin: 0; padding: 0; }
  html, body {
    width: 1200px; height: 900px; overflow: hidden;
    background: var(--page-bg);
  }
  .canvas {
    position: relative; width: 1200px; height: 900px;
    background: radial-gradient(ellipse at 50% 60%, #e4e4e4 0%, var(--page-bg) 70%, #b9b9b9 100%);
  }
  .book {
    position: absolute; left: 100px; top: 110px;
    width: 1000px; height: 680px;
    display: flex;
    box-shadow: 0 18px 40px rgba(0,0,0,.28);
  }
  /* Spine */
  .spine {
    position: relative; width: 90px; height: 100%;
    overflow: hidden;
    background: linear-gradient(90deg, var(--steel-dark) 0%, var(--steel-light) 35%, #f2f3f5 50%, var(--steel-light) 65%, var(--steel-mid) 100%);
    border-right: 1px solid rgba(0,0,0,.35);
    display: flex; flex-direction: row-reverse;
    justify-content: center; align-items: flex-start;
    gap: 6px; padding-top: 26px;
  }
  .spine-title {
    writing-mode: vertical-rl;
    font-family: "Anton", sans-serif; font-size: 44px; line-height: 1;
    color: var(--year-red); text-transform: uppercase; letter-spacing: 1px;
    white-space: nowrap;
  }
  .spine-author {
    writing-mode: vertical-rl;
    font-family: "Tinos", serif; font-weight: 700; font-size: 14px; line-height: 1;
    color: var(--author-ink); white-space: nowrap;
    padding-top: 60px;
  }
  /* Front cover */
  .cover {
    position: relative; flex: 1; height: 100%; overflow: hidden;
  }
  .cover-photo {
    position: absolute; inset: 0;
    background:
      linear-gradient(180deg, rgba(29,95,176,.9) 0%, rgba(29,95,176,.35) 12%, transparent 22%),
      linear-gradient(100deg, var(--steel-light) 0%, var(--steel-mid) 45%, var(--steel-dark) 75%, var(--steel-mid) 100%);
  }
  .copyright {
    position: absolute; left: 38px; top: 18px;
    font-family: "Tinos", serif; font-size: 15px; letter-spacing: .5px;
    color: var(--copyright-gold);
  }
  .title-panel {
    position: absolute; left: 30px; top: 52px;
    width: 600px; height: 470px;
    background: var(--cover-red);
  }
  .title {
    position: absolute; left: 30px; top: 18px;
    font-family: "Anton", sans-serif; color: var(--title-white);
    font-size: 88px; line-height: 1.0; letter-spacing: 1px;
    text-transform: uppercase; font-weight: 400;
  }
  .title span { display: block; }
  .subtitle {
    position: absolute; left: 34px; top: 312px; width: 550px;
    font-family: "Tinos", serif; color: var(--title-white);
  }
  .subtitle .lead { font-weight: 700; font-size: 18px; text-transform: uppercase; }
  .subtitle .topics { font-weight: 700; font-size: 17px; margin-top: 6px; line-height: 1.3; }
  .edition-year {
    position: absolute; right: 24px; bottom: -36px;
    font-family: "Anton", sans-serif; font-size: 250px; line-height: 1;
    color: var(--year-red); letter-spacing: -4px;
  }
  .seal {
    position: absolute; right: 70px; top: 70px;
    width: 90px; height: 90px; border-radius: 50%;
    background: var(--badge-navy); border: 4px solid var(--steel-light);
  }
</style>
</head>
<body>
  <main class="canvas">
    <div class="book">
      <aside class="spine" aria-label="Book spine">
        <p class="spine-title">Patrol Deputy Statute Digest</p>
        <p class="spine-author">Lieutenant Daniel R. Whitcombe, Esq. &nbsp; The Law Office of Daniel R. Whitcombe</p>
      </aside>
      <section class="cover" aria-label="Patrol Deputy Statute Digest 2017 front cover">
        <div class="cover-photo" role="img" aria-label="Photo of a patrol car with blue emergency lights and polished steel body"></div>
        <p class="copyright">© 2016 Brightwater Consulting LLC &nbsp; All Rights Reserved</p>
        <div class="title-panel">
          <h1 class="title">
            <span>Patrol Deputy</span>
            <span>Statute</span>
            <span>Digest</span>
          </h1>
          <div class="subtitle">
            <p class="lead">Massachusetts Patrol Deputy’s Guide to:</p>
            <p class="topics">Criminal Procedure, Statutory Law,<br>Motor Vehicle Law and Juvenile Law</p>
          </div>
        </div>
        <div class="seal" aria-hidden="true"></div>
        <p class="edition-year">2017</p>
      </section>
    </div>
  </main>
</body>
</html>
```